HTML Digital Sign layout and code (one page)...save us from the 60's!

Digital Sign for Headquarters Entrance

HTML Digital Sign layout (one page)...save us from the 60's!

Good Day Designers!

We have decided to install Digital Signage in our headquarters building that will replace the “felt boards” that the administrative staff use at our building entrances.

Instead of the information being displayed on the archaic sign boards, it will be presented on a landscaped 50inch LCD screen running at 1920x1080

We are looking for a one page HTML design that encompass the following elements:

+ Our Logo
+ Our Company Name (HRV Solvance)
+ Our "Tag Line" - "Ideas shaped by practice, quality shaped by dedication"
+ Date and Time
+ A space for Today’s Birthdays (which could be up to 4 people)
+ A space for Today’s Anniversaries (which could be up to 4 people)
+ A space for Today’s Visitor (which could be up to 2 people)
+ A space for a Picture of the Day
+ A space for Weather Forecast (perhaps a graphic)
+ A small "banner" section or strip for scrolling Notices / Alerts (perhaps at the bottom of the page?)

The deliverables for the layout need to include the HTML, applicable CSS, HTML code, etc. We need this to be relatively turnkey.

I have included in the contest package a hi-res JPG and AI for our Company Logo.

From a color pallet perspective:

Light Blue:
RGB - 21, 191,242
HEX - #15BFF2

Dark Blue:
RGB - 0, 70, 154
HEX - #00469A

Additionally, I have done a contest like this before (for another company I was at) and have included a screen shot of that final display.

PLEASE NOTE: IT DOES NOT HAVE TO LOOK EXACTLY LIKE THE ATTACHED SCREEN SHOT FROM THE PREVIOUS CONTEST. Including the screenshot was just to give you a general idea of some inspiration and objectives.

Feedback and questions are encouraged.

Target Market(s)

Our Employees

Industry/Entity Type

Digital

Number of Pages Required

1 page

Requirements
Must have
• + Our Logo
• + Our Company Name (HRV Solvance)
• + Our "Tag Line" - "Ideas shaped by practice, quality shaped by dedication"
• + Date and Time
• + A space for Today’s Birthdays (which could be up to 4 people)
• + A space for Today’s Anniversaries (which could be up to 4 people)
• + A space for Today’s Visitor (which could be up to 2 people)
• + A space for a Picture of the Day
• + A space for Weather Forecast (perhaps a graphic)
• + A small "banner" section or strip for scrolling Notices / Alerts (perhaps at the bottom of the page?)

```html
<!DOCTYPE html>
<html lang="en">
<head>
<meta charset="utf-8">
<title>HRV Solvance – Entrance Sign</title>
<link rel="stylesheet" href="https://fonts.googleapis.com/css2?family=Source+Sans+3:wght@300;400;600;700&display=swap">
<style>
  :root {
    --sky-top: #4aa3cf;
    --sky-mid: #8cc6e2;
    --sky-low: #3f93c4;
    --navy: #14275e;
    --royal: #1c3b8f;
    --photo-a: #5a7593;
    --photo-b: #8ea5bb;
    --cyan: #0b8cca;
    --indigo: #243f8c;
    --alert: #2352c9;
    --deep: #173a6e;
    --white: #ffffff;
    --brand-dark: #00469A;
    --bouquet: rgba(255,255,255,.35);
  }
  html, body { margin: 0; padding: 0; overflow: hidden; }
  body { width: 1200px; height: 675px; font-family: "Source Sans 3", "Segoe UI", sans-serif; color: var(--white); }
  .sign { position: relative; width: 1200px; height: 675px; overflow: hidden; }
  .sky {
    position: absolute; inset: 0;
    background:
      radial-gradient(ellipse 500px 180px at 780px 40px, rgba(255,255,255,.85), rgba(255,255,255,0) 70%),
      radial-gradient(ellipse 380px 160px at 220px 170px, rgba(255,255,255,.6), rgba(255,255,255,0) 70%),
      radial-gradient(ellipse 520px 200px at 700px 660px, rgba(255,255,255,.55), rgba(255,255,255,0) 70%),
      linear-gradient(180deg, var(--sky-top) 0%, var(--sky-mid) 50%, var(--sky-low) 100%);
  }
  .brand {
    position: absolute; left: 0; top: 217px; width: 304px; height: 198px;
    background: var(--white); text-align: center; color: var(--brand-dark);
  }
  .brand-name { margin: 44px 0 0; font-size: 42px; font-weight: 700; letter-spacing: 1px; line-height: 1; }
  .brand-tagline { margin: 30px 0 0; font-size: 16px; font-weight: 400; line-height: 1.3; color: var(--brand-dark); }
  .tile { position: absolute; box-sizing: border-box; }
  .tile h2 { margin: 0; font-weight: 300; font-size: 29px; line-height: 1.1; }
  .names { list-style: none; margin: 14px 0 0; padding: 0; font-weight: 300; font-size: 19px; line-height: 23px; }
  .weather { left: 322px; top: 56px; width: 205px; height: 177px; background: var(--navy); text-align: center; padding-top: 28px; }
  .weather svg { display: block; margin: 0 auto; }
  .weather-city { margin: 12px 0 0; font-size: 16px; font-weight: 300; }
  .weather-now { margin: 0; font-size: 25px; font-weight: 300; line-height: 1.1; }
  .weather-now sup { font-size: 11px; }
  .clock { left: 533px; top: 56px; width: 206px; height: 177px; background: var(--royal); padding: 57px 0 0 22px; }
  .clock-day { margin: 0; font-size: 29px; font-weight: 300; line-height: 1; }
  .clock-date { margin: 2px 0 0; font-size: 20px; font-weight: 300; }
  .photo { left: 744px; top: 56px; width: 423px; height: 177px; padding: 52px 0 0 17px;
    background: linear-gradient(120deg, var(--photo-a) 0%, var(--photo-b) 60%, var(--photo-a) 100%); }
  .photo p { margin: 6px 0 0; font-size: 16.5px; font-weight: 300; line-height: 19px; width: 310px; }
  .birthdays { left: 322px; top: 242px; width: 417px; height: 183px; background: var(--cyan); padding: 28px 0 0 22px; }
  .visitors { left: 746px; top: 242px; width: 209px; height: 183px; background: var(--indigo); padding: 28px 0 0 12px; }
  .visitors .names { font-size: 17px; line-height: 20px; margin-top: 12px; }
  .alert { left: 963px; top: 242px; width: 204px; height: 374px; background: var(--alert); text-align: center; padding-top: 22px; }
  .alert svg { display: block; margin: 0 auto; }
  .alert p { margin: 42px 0 0; font-size: 25px; font-weight: 300; line-height: 31px; }
  .anniversaries { left: 322px; top: 433px; width: 417px; height: 183px; background: var(--deep); padding: 28px 0 0 22px; }
  .blank { left: 746px; top: 433px; width: 209px; height: 183px; background: var(--white); }
  .icon { position: absolute; }
  .cake { right: 34px; top: 78px; }
  .bouquet { right: 34px; top: 80px; width: 76px; height: 82px; background: var(--bouquet); }
</style>
</head>
<body>
<main class="sign">
  <div class="sky" role="img" aria-label="Bright blue sky with soft white clouds"></div>

  <header class="brand">
    <p class="brand-name">HRV Solvance</p>
    <p class="brand-tagline">Ideas shaped by practice,<br>quality shaped by dedication.</p>
  </header>

  <section class="tile weather">
    <svg width="114" height="66" viewBox="0 0 114 66" aria-hidden="true">
      <path d="M28 60 H88 A20 20 0 0 0 90 20 A28 28 0 0 0 40 14 A22 22 0 0 0 28 60 Z" fill="none" stroke="#fff" stroke-width="8" stroke-linejoin="round"/>
    </svg>
    <p class="weather-city">San Antonio</p>
    <p class="weather-now">77<sup>°F</sup>Cloudy</p>
  </section>

  <section class="tile clock">
    <p class="clock-day">Saturday</p>
    <p class="clock-date">Sep 6, 4:45am CDT</p>
  </section>

  <section class="tile photo" role="img" aria-label="Picture of the day: a passenger jet climbing through the clouds">
    <h2>Picture of the day</h2>
    <p>Lorem ipsum dolor sit amet, consectetur adipiscing elit, sed do eiusmod tempor.</p>
  </section>

  <section class="tile birthdays">
    <h2>Today’s Birthdays</h2>
    <ul class="names"><li>Jack Nickeman</li><li>Robert Downing</li><li>Julia Albert</li><li>Feren Allen</li></ul>
    <svg class="icon cake" width="88" height="84" viewBox="0 0 88 84" aria-hidden="true" fill="#fff">
      <path d="M44 2 C50 10 48 16 44 16 C40 16 38 10 44 2 Z"/>
      <rect x="40" y="19" width="8" height="14"/>
      <rect x="4" y="34" width="80" height="14" rx="3"/>
      <rect x="4" y="51" width="80" height="12"/>
      <rect x="4" y="66" width="80" height="10"/>
      <rect x="0" y="78" width="88" height="6" rx="3"/>
    </svg>
  </section>

  <section class="tile visitors">
    <h2>Today’s visitors</h2>
    <ul class="names"><li>Adam Mitchell</li><li>Rebecca Kilton</li></ul>
  </section>

  <aside class="tile alert">
    <svg width="74" height="68" viewBox="0 0 74 68" aria-hidden="true">
      <path d="M37 4 L71 64 H3 Z" fill="#fff" stroke="#fff" stroke-width="6" stroke-linejoin="round"/>
      <rect x="33" y="22" width="8" height="24" rx="4" fill="var(--alert)"/>
      <circle cx="37" cy="54" r="4.5" fill="var(--alert)"/>
    </svg>
    <p>Pay attention<br>while walking,<br>your Chatterbox<br>status update<br>can wait.</p>
  </aside>

  <section class="tile anniversaries">
    <h2>Today’s Anniversaries</h2>
    <ul class="names"><li>Josie Dersson</li><li>Cristian Culucci</li><li>Fabio Carravo</li><li>Sam Anderson</li></ul>
    <div class="icon bouquet" role="img" aria-label="Bouquet of flowers"></div>
  </section>

  <div class="tile blank"></div>
</main>
</body>
</html>
```